Paying WELL above market rates to find the very best Powerpoint Designer for keynote presentations..

Large cap tech company on the west coast is looking to bring a fresh and innovative new look to a series of keynote presentations. There will be 4 x 30 slide decks over the next 3 months. We are the whale customer you want to land!...We are prepared to pay WELL about market rates to attract the very best designers to work on our project.

Attached are the slides I would like repainted... we did these internally, but I need them to be redesigned....

Target Market(s)

Enterprise Corporate

Industry/Entity Type

It Company

```html
<!DOCTYPE html>
<html lang="en">
<head>
<meta charset="utf-8">
<title>Timeline Slide</title>
<link href="https://fonts.googleapis.com/css2?family=Carlito:wght@400;700&display=swap" rel="stylesheet">
<style>
  :root {
    --orange: #f5821f;
    --orange-deep: #f1620d;
    --ink: #262626;
    --slate: #5e5e5e;
    --text-grey: #7a7a7a;
    --rail: #dcdcdc;
    --stem: #c9c9c9;
    --ghost: #f1f1f1;
    --paper: #ffffff;
  }
  * { box-sizing: border-box; margin: 0; padding: 0; }
  html, body { width: 1200px; height: 900px; overflow: hidden; background: var(--paper); }
  body { font-family: "Carlito", "Calibri", sans-serif; }
  .slide { position: relative; width: 1200px; height: 900px; overflow: hidden;
    background: radial-gradient(circle at 15% 35%, #f7f7f7 0, var(--paper) 45%); }

  .backdrop-art { position: absolute; left: 800px; top: 90px; width: 400px; height: 765px;
    background: linear-gradient(180deg, var(--ghost), #f7f7f7);
    border-radius: 140px 0 0 60px; }

  .header { position: absolute; left: 0; top: 0; width: 1200px; height: 69px;
    background: var(--orange); border-bottom: 4px solid var(--slate); }
  .header-title { position: absolute; left: 14px; top: 10px; color: #fff;
    font-weight: 700; font-size: 37px; letter-spacing: 0.3px; }
  .header-badge { position: absolute; left: 1086px; top: -8px; width: 108px; height: 108px;
    border-radius: 50%; background: var(--orange); border: 5px solid var(--slate); }

  .footer { position: absolute; left: 0; top: 855px; width: 1200px; height: 45px; background: var(--slate); }
  .footer-copy { position: absolute; left: 9px; top: 8px; color: #fff; font-size: 24.5px; }
  .page-number { position: absolute; left: 1107px; top: 824px; width: 72px; height: 72px;
    border-radius: 50%; background: var(--orange); border: 5px solid var(--slate);
    color: #fff; font-weight: 700; font-size: 24px; display: flex; align-items: center; justify-content: center; }

  .timeline { position: absolute; left: 0; top: 0; }

  .milestone-year { position: absolute; width: 78px; height: 78px; border-radius: 50%;
    color: #fff; font-weight: 700; font-size: 24px; display: flex; align-items: center; justify-content: center; }
  .milestone-year.is-upper { background: var(--orange-deep); }
  .milestone-year.is-lower { background: var(--ink); }

  .milestone-copy { position: absolute; }
  .milestone-subtitle { color: var(--orange); font-weight: 700; font-size: 25px; line-height: 27px; }
  .milestone-desc { color: var(--text-grey); font-size: 20.5px; line-height: 27px; white-space: nowrap; }
</style>
</head>
<body>
<div class="slide">
  <div class="backdrop-art" role="img" aria-label="Faint large trophy silhouette in the background"></div>

  <header class="header">
    <h1 class="header-title">PERSENTATION TITLE HERE</h1>
    <div class="header-badge"></div>
  </header>

  <svg class="timeline" width="1200" height="900" aria-hidden="true">
    <line x1="148" y1="491" x2="1085" y2="491" stroke="var(--rail)" stroke-width="3"/>
    <line x1="148.5" y1="372" x2="148.5" y2="491" stroke="var(--stem)" stroke-width="2.5"/>
    <line x1="549" y1="372" x2="549" y2="491" stroke="var(--stem)" stroke-width="2.5"/>
    <line x1="954" y1="372" x2="954" y2="491" stroke="var(--stem)" stroke-width="2.5"/>
    <line x1="280.5" y1="491" x2="280.5" y2="614" stroke="var(--stem)" stroke-width="2.5"/>
    <line x1="681" y1="491" x2="681" y2="614" stroke="var(--stem)" stroke-width="2.5"/>
    <line x1="1084.5" y1="491" x2="1084.5" y2="614" stroke="var(--stem)" stroke-width="2.5"/>
    <circle cx="148.5" cy="491" r="7" fill="var(--orange-deep)"/>
    <circle cx="549" cy="491" r="7" fill="var(--orange-deep)"/>
    <circle cx="954" cy="491" r="7" fill="var(--orange-deep)"/>
    <circle cx="280.5" cy="491" r="7.5" fill="var(--ink)"/>
    <circle cx="681" cy="491" r="7.5" fill="var(--ink)"/>
    <circle cx="1084.5" cy="491" r="7.5" fill="var(--ink)"/>
    <circle cx="412.5" cy="491" r="4.5" fill="var(--ink)"/>
    <circle cx="807" cy="491" r="4.5" fill="var(--ink)"/>
  </svg>

  <div class="milestone-year is-upper" style="left:109.5px; top:333px;">2007</div>
  <div class="milestone-year is-upper" style="left:510px; top:333px;">2008</div>
  <div class="milestone-year is-upper" style="left:915px; top:333px;">2009</div>
  <div class="milestone-year is-lower" style="left:241.5px; top:574.5px;">2010</div>
  <div class="milestone-year is-lower" style="left:642px; top:574.5px;">2011</div>
  <div class="milestone-year is-lower" style="left:1045.5px; top:574.5px;">2012</div>

  <div class="milestone-copy" style="left:88px; top:233px;">
    <h2 class="milestone-subtitle">Subtitle Here</h2>
    <p class="milestone-desc">Description Text here<br>Description Text</p>
  </div>
  <div class="milestone-copy" style="left:486px; top:242px;">
    <h2 class="milestone-subtitle">Subtitle Here</h2>
    <p class="milestone-desc">Description Text here<br>Description Text</p>
  </div>
  <div class="milestone-copy" style="left:891px; top:242px;">
    <h2 class="milestone-subtitle">Subtitle Here</h2>
    <p class="milestone-desc">Description Text here<br>Description Text</p>
  </div>
  <div class="milestone-copy" style="left:214px; top:676px;">
    <h2 class="milestone-subtitle">Subtitle Here</h2>
    <p class="milestone-desc">Description Text here<br>Description Text</p>
  </div>
  <div class="milestone-copy" style="left:598px; top:676px;">
    <h2 class="milestone-subtitle">Subtitle Here</h2>
    <p class="milestone-desc">Description Text here<br>Description Text</p>
  </div>
  <div class="milestone-copy" style="left:1014px; top:676px;">
    <h2 class="milestone-subtitle">Subtitle Here</h2>
    <p class="milestone-desc">Description Text here<br>Description Text</p>
  </div>

  <footer class="footer">
    <p class="footer-copy">Copyright text here</p>
  </footer>
  <div class="page-number">01</div>
</div>
</body>
</html>
```